KV Group

We need a new website for our company and since we had a very good work done for our logo in this site, we're back for the entire job.

Our company name is Marlowe Capital Group. We're adding files of examples of what we have done today. In my opinion we need a more attention lock in the site but yet financial simple work.

Our files (attached) will let you know what we have so far. We need a complete change but the colours should be the same, however you can change them not running away to far from the original, and of course matching with the logo.

We need examples for 3 kind of layouts.

- A HOME welcome layout
- An internal Layout with sidebar
- And internal Layout wide

We can buy image licenses if needed for assets.
Actually there are 5 slide images placed on the Welcome HOME, we need those there, but you can improve with better images to match the new website!!!

Target Market(s)

Clients looking for financial advisers, tax and funds specialist, currency advisers

Industry/Entity Type

Financial

Requirements
Must have
• all the fonts must be in accordance with the financial market sites........the welcome home page must be precise, neat and information accurate........the menu should be elegant........main focus on the Home page, should be also the PRIVATE ACCESS box log in.......

```html
<!DOCTYPE html>
<html lang="en">
<head>
<meta charset="utf-8">
<title>Marlowe Capital Group</title>
<link href="https://fonts.googleapis.com/css2?family=Cabin:wght@400;600;700&family=Cinzel:wght@400;600&family=Open+Sans:wght@400;600;700&family=Source+Sans+3:wght@400;600&display=swap" rel="stylesheet">
<style>
:root{
  --brown:#3d2309;
  --rust:#8a3d0a;
  --orange:#f47b20;
  --yellow:#f5b323;
  --text:#2b2b2b;
  --grey:#e5e5e5;
  --up:#2e9a2e;
  --down:#d92525;
}
*{margin:0;padding:0;box-sizing:border-box}
html,body{width:879px;height:1200px;overflow:hidden;background:#fff}
body{position:relative;font-family:"Open Sans",Arial,sans-serif;color:var(--text)}
.abs{position:absolute}

.topbar{left:0;top:0;width:879px;height:26px;background:var(--brown)}
.topbar-curve{left:0;top:0;width:258px;height:26px;background:#fff;border-top-right-radius:46px 26px}
.pill{position:absolute;height:18px;border-radius:9px;background:var(--orange);color:#fff;font-size:7.5px;display:flex;align-items:center;justify-content:center;gap:4px}
.pill::before{content:"";width:4px;height:4px;background:#fff}

.brand{left:158px;top:30px;display:flex;align-items:center;gap:7px}
.brand-mark{width:16px;height:16px;background:var(--orange)}
.brand-name{font-family:"Cabin",sans-serif;font-weight:600;font-size:12.5px;color:var(--brown);letter-spacing:.3px}

.nav{left:319px;top:46px;display:flex;align-items:center;font-family:"Cinzel",serif;font-size:11.5px;color:#1a1a1a}
.nav a{color:inherit;text-decoration:none;padding:2px 0;margin-right:18px}
.nav a.active{background:var(--brown);color:#fff;border-radius:10px;padding:2px 12px;margin-left:-8px;margin-right:8px}

.hero{left:158px;top:86px;width:563px;height:254px;background:linear-gradient(100deg,#d9c1a2 0%,#b59a7c 25%,#5a4f52 50%,#26303f 75%,#1f2633 100%)}
.hero-arrow{top:200px;font-size:16px;color:#fff;opacity:.8}
.hero-title{left:202px;top:196px;font-family:"Source Sans 3",sans-serif;font-weight:600;font-size:21px;color:#fff;letter-spacing:-.2px;text-shadow:0 1px 2px rgba(0,0,0,.4)}
.hero-text{left:204px;top:223px;width:300px;font-family:"Source Sans 3",sans-serif;font-size:10.3px;line-height:13.2px;color:#fff;text-shadow:0 1px 2px rgba(0,0,0,.5)}
.hero-btn{left:204px;top:270px;width:188px;height:28px;background:var(--yellow);color:var(--brown);font-family:"Source Sans 3",sans-serif;font-weight:600;font-size:11px;display:flex;align-items:center;justify-content:center;box-shadow:0 2px 3px rgba(0,0,0,.3)}

.access{left:538px;top:308px;width:170px;height:133px;background:var(--rust);box-shadow:0 4px 6px rgba(0,0,0,.15)}
.access-head{height:34px;background:var(--brown);color:#fff;font-family:"Source Sans 3",sans-serif;font-size:15.5px;padding:9px 0 0 18px}
.field{position:absolute;left:18px;width:132px;height:19px;background:#fff;font-size:7.5px;color:#888;padding:4px 0 0 7px}
.login{position:absolute;left:18px;top:94px;width:132px;height:24px;background:var(--orange);color:#fff;font-family:"Source Sans 3",sans-serif;font-weight:600;font-size:11px;display:flex;align-items:center;justify-content:center}

.welcome-title{left:158px;top:368px;font-family:"Cabin",sans-serif;font-size:17.5px;color:var(--brown)}
.welcome-text{left:158px;top:397px;width:352px;font-size:8.1px;line-height:11px;color:#222}

.card{top:476px;width:180px;height:180px;background:#fff;border:1px solid #ddd;box-shadow:0 2px 4px rgba(0,0,0,.08)}
.card h3{font-family:"Cabin",sans-serif;font-weight:600;font-size:11px;color:var(--brown);text-align:center;margin-top:11px}
.card-img{position:absolute;left:8px;top:38px;width:163px;height:76px}
.card p{position:absolute;left:10px;top:121px;width:159px;text-align:center;font-size:7.9px;line-height:9.4px;color:#333}
.card-foot{position:absolute;left:0;bottom:-1px;width:178px;height:3px;background:var(--orange)}
.card-tab{position:absolute;left:0;bottom:0;width:72px;height:17px;background:var(--orange);clip-path:polygon(0 0,62% 0,100% 100%,0 100%);color:#fff;font-size:7px;padding:4px 0 0 10px}

.ticker{left:0;top:691px;width:879px;height:23px;background:var(--grey)}
.rate{position:absolute;top:8px;font-size:5.8px;font-weight:600;color:var(--brown)}
.rate .up{color:var(--up)}
.rate .down{color:var(--down)}

.verified{left:158px;top:727px;font-family:"Cabin",sans-serif;font-size:19px;color:#1a1a1a}
.badge{position:absolute;top:730px;height:25px}

.footer{left:0;top:768px;width:879px;height:297px;background:var(--brown)}
.col{position:absolute;top:46px}
.col h4{font-family:"Cabin",sans-serif;font-weight:700;font-size:11px;color:var(--orange);display:flex;align-items:center;gap:3px;margin-bottom:10px}
.col ul{list-style:none}
.col li{font-size:7.3px;color:#fff;height:22px;padding-top:1px;position:relative;padding-left:8px}
.col li::before{content:"";position:absolute;left:0;top:4px;width:3.5px;height:3.5px;background:#fff}
.col li::after{content:"";position:absolute;left:0;top:14px;width:var(--rule,62px);border-top:1px dashed #bfa98f}
.col li:last-child::after{display:none}
.divider{position:absolute;top:18px;width:1px;height:256px;background:#5a3a1a}
.social{position:absolute;width:10px;height:10px;border-radius:50%;background:#fff}
.foot-pill{position:absolute;height:17px;border-radius:9px;background:var(--orange);color:#fff;font-size:7.3px;display:flex;align-items:center;justify-content:center;gap:4px}
.foot-pill::before{content:"";width:4px;height:4px;background:#fff}
.copy-tab{left:306px;top:1048px;width:260px;height:18px;background:#fff;clip-path:polygon(6% 0,94% 0,100% 100%,0 100%)}
.copy{left:0;top:1058px;width:879px;text-align:center;font-size:7.5px;color:#555}
.legal{left:160px;width:560px;text-align:center;font-size:5.7px;line-height:7.6px;color:#444}
</style>
</head>
<body>

<header>
  <div class="abs topbar"></div>
  <div class="abs topbar-curve"></div>
  <div class="pill" style="left:575px;top:4px;width:71px">Apply Now</div>
  <div class="pill" style="left:650px;top:4px;width:71px">Contact Us</div>

  <div class="abs brand">
    <span class="brand-mark"></span>
    <span class="brand-name">Marlowe Capital Group</span>
  </div>

  <nav class="abs nav">
    <a href="#">Home</a>
    <a href="#" class="active">About</a>
    <a href="#">Investment</a>
    <a href="#">Funds</a>
    <a href="#">Brokerage</a>
    <a href="#">Exchange</a>
    <a href="#" style="margin-right:0">Accounts</a>
  </nav>
</header>

<section>
  <div class="abs hero" role="img" aria-label="Photo of private bankers in suits reviewing documents together at a desk"></div>
  <div class="abs hero-arrow" style="left:178px">&#8249;</div>
  <div class="abs hero-arrow" style="left:691px">&#8250;</div>
  <h1 class="abs hero-title">TEAMWORK FOR YOUR BENEFIT</h1>
  <p class="abs hero-text">Our dedicated Private Bankers, will proactively keep you up to date with relevant information and provide a financial overview that enables you to make lorem ipsum dummy text...</p>
  <div class="abs hero-btn">SUBSCRIBE OUR SERVICES</div>

  <div class="abs access">
    <div class="access-head">PRIVATE ACCESS</div>
    <div class="field" style="top:43px">Acc. Number</div>
    <div class="field" style="top:67px">Acc. Password</div>
    <div class="login">LOGIN TO ACCOUNT</div>
  </div>

  <h2 class="abs welcome-title">Welcome to Marlowe Capital Group</h2>
  <p class="abs welcome-text">Lorem ipsum dolor sit amet, consectetur adipisicing elit, sed do eiusmod tempor incididunt ut labore et dolore magna aliqua. Ut enim ad minim veniam, nostrud exercitation ullamco laboris nisi ut aliquip commodo consequatfugiat nulla pariatur. Excepteu Lorem ipsum dolor sit amet, consectetur adipisicing elit, sed eiusmod tempor incididunt ut labore</p>
</section>

<section>
  <article class="abs card" style="left:158px">
    <h3>Management &amp; Strategy</h3>
    <div class="card-img" role="img" aria-label="Photo of hands working over printed bar charts on a desk" style="background:linear-gradient(135deg,#f2f2f0,#d8dcd2 55%,#a9c98a)"></div>
    <p>Lorem ipsum dolor sit Lorem ipsum dolor sit amet onsectetur amet dolor sit Lorem ipsum dolor sit amet onsectetur</p>
    <div class="card-foot"></div><div class="card-tab">learn more</div>
  </article>
  <article class="abs card" style="left:350px">
    <h3>Funds</h3>
    <div class="card-img" role="img" aria-label="Illustration of a golden dollar sign over financial charts" style="background:linear-gradient(135deg,#dfe6ef,#e9c866 50%,#b7c7dc)"></div>
    <p>Lorem ipsum dolor sit Lorem ipsum dolor sit amet onsectetur amet dolor sit Lorem ipsum dolor sit amet onsectetur</p>
    <div class="card-foot"></div><div class="card-tab">learn more</div>
  </article>
  <article class="abs card" style="left:542px">
    <h3>Currency Exchange</h3>
    <div class="card-img" role="img" aria-label="Photo of glass office towers against a blue sky" style="background:linear-gradient(160deg,#a9c3dc,#3f6488 55%,#1e3452)"></div>
    <p>Lorem ipsum dolor sit Lorem ipsum dolor sit amet onsectetur amet dolor sit Lorem ipsum dolor sit amet onsectetur</p>
    <div class="card-foot"></div><div class="card-tab">learn more</div>
  </article>
</section>

<div class="abs ticker">
  <span class="rate" style="left:160px">GBP / UAH = <span class="up">12.65761 &#9650;</span></span>
  <span class="rate" style="left:242px">GBP / UAH = <span class="down">12.65761 &#9660;</span></span>
  <span class="rate" style="left:324px">GBP / UAH = <span class="up">12.65761 &#9650;</span></span>
  <span class="rate" style="left:406px">GBP / UAH = <span class="up">12.65761 &#9650;</span></span>
  <span class="rate" style="left:488px">GBP / UAH = <span class="down">12.65761 &#9660;</span></span>
  <span class="rate" style="left:570px">GBP / UAH = <span class="up">12.65761 &#9650;</span></span>
  <span class="rate" style="left:652px">GBP / UAH = <span class="up">12.65761 &#9650;</span></span>
</div>

<h2 class="abs verified">Verified and Protected by</h2>
<svg class="badge" style="left:454px" width="50" height="25" aria-hidden="true"><rect x="1" y="4" width="48" height="17" rx="8.5" fill="none" stroke="#b22" stroke-width="1.5"/></svg>
<svg class="badge" style="left:531px" width="50" height="25" aria-hidden="true"><rect x="1" y="5" width="48" height="15" rx="2" fill="#6aa23a"/></svg>
<svg class="badge" style="left:612px" width="42" height="25" aria-hidden="true"><rect x="1" y="5" width="40" height="15" fill="#1f4fa3"/></svg>
<svg class="badge" style="left:697px" width="25" height="25" aria-hidden="true"><circle cx="12.5" cy="12.5" r="12" fill="#1d3a6e"/></svg>

<footer class="abs footer">
  <div class="divider" style="left:231px"></div>
  <div class="divider" style="left:395px"></div>
  <div class="divider" style="left:490px"></div>
  <div class="divider" style="left:634px"></div>

  <div class="col" style="left:158px">
    <h4><svg width="10" height="10" viewBox="0 0 10 10"><path d="M1 5l3 3 5-7" fill="none" stroke="#f47b20" stroke-width="2"/></svg>About Us</h4>
    <ul><li>History</li><li>Expertize</li><li>Identity</li><li>Strategy</li><li>Contact us</li></ul>
  </div>
  <div class="col" style="left:245px;--rule:130px">
    <h4><svg width="10" height="10" viewBox="0 0 10 10"><path d="M1 5l3 3 5-7" fill="none" stroke="#f47b20" stroke-width="2"/></svg>Investments</h4>
    <ul><li>Term Deposits</li><li>Management &amp; Strategy</li><li>Client Relations</li><li>Financial Privacy</li><li>Tax Advice</li><li>Wealth Analysis &amp; Financial Planning</li><li>Active Adisory Group</li><li>Manager Selection Servoces</li><li>Provate Equity</li></ul>
  </div>
  <div class="col" style="left:414px">
    <h4><svg width="10" height="10" viewBox="0 0 10 10"><path d="M1 5l3 3 5-7" fill="none" stroke="#f47b20" stroke-width="2"/></svg>Funds</h4>
    <ul><li>History</li><li>Expertize</li><li>Identity</li><li>Strategy</li><li>Contact us</li></ul>
  </div>
  <div class="col" style="left:507px">
    <h4><svg width="10" height="10" viewBox="0 0 10 10"><path d="M1 5l3 3 5-7" fill="none" stroke="#f47b20" stroke-width="2"/></svg>Currency Exchange</h4>
    <ul><li>Forign Exchange</li><li>Fx Forward</li><li>Fx Options</li></ul>
  </div>
  <div class="col" style="left:507px;top:142px">
    <h4><svg width="10" height="10" viewBox="0 0 10 10"><path d="M1 5l3 3 5-7" fill="none" stroke="#f47b20" stroke-width="2"/></svg>Accounts</h4>
  </div>
  <div class="foot-pill" style="left:505px;top:158px;width:71px">Apply Now</div>
  <div class="foot-pill" style="left:504px;top:178px;width:84px">Private Access</div>

  <div class="col" style="left:650px">
    <h4><svg width="10" height="10" viewBox="0 0 10 10"><path d="M1 5l3 3 5-7" fill="none" stroke="#f47b20" stroke-width="2"/></svg>Brokerage</h4>
    <ul><li>Institutional</li><li>Research</li><li>Traiding</li></ul>
  </div>
  <span class="social" style="left:654px;top:142px"></span>
  <span class="social" style="left:672px;top:142px"></span>
  <span class="social" style="left:689px;top:142px"></span>
</footer>

<div class="abs copy-tab"></div>
<p class="abs copy">© 2013 all right reserved with KV Group - Terms</p>

<p class="abs legal" style="top:1094px">Lorem ipsum dolor sit amet, consectetur adipiscing elit. In fermentum dolor non augue pretium egestas. Donec sem eros, tincidunt at congue ut, posuere sit amet est. Vivamus scelerisque viverra odio sit amet laoreet. Ut nec neque non justo rutrum tempor lobortis eu ante. Aliquam sagittis, nibh quis commodo auctor, risus mauris laoreet lectus, id facilisis libero odio nec enim. Sed id ligula adipiscing purus lacinia aliquet. Sed eu est non nisl vehicula bibendum congue sit amet enim.</p>
<p class="abs legal" style="top:1126px">Lorem ipsum dolor sit amet, consectetur adipiscing elit. In fermentum dolor non augue pretium egestas. Donec sem eros, tincidunt at congue ut, posuere sit amet est vivamus scelerisque viverra odio sit amet laoreet. Ut nec neque non justo rutrum tempor lobortis eu ante. Aliquam sagittis, nibh quis commodo auctor, risus mauris laoreet lectus, id facilisis libero odio nec enim. Sed id ligula adipiscing purus lacinia aliquet..</p>

</body>
</html>
```